Modern luxury trendy cosmetics label

Looking for a cosmetics packaging label design. We are looking for a professionel, modern and luxury look like Helena Voskuijl, Meadowfern Apothecary, Autumn Vale, Gordon Ellis Marsh, Quba, Oskar + Brandt, Velumo, Dizzy Walrus, the plainspoken, lumires de charme.Name of product: Alpine Edelweiss Wrap - No-Needle Contour Treatment Ingredients that have scientific proof of anti aging: Cherry blossom extact, collegen, hyaluronic acid, coconut oil. Color of product itself: Pastel pink. Smell: Cherry blossom. Colors of label: simple and black and white or some subtle colors.

Target Market(s)

Women, luxury market, modern women, young and old women

Industry/Entity Type

Cosmetics

Font styles to use
Sans Serif

Colors

Designer to choose colors to be used in the design.

Requirements
Must have
• A modern look, professional, cosmetics, beauty, professional market, original

```html
<!DOCTYPE html>
<html lang="en">
<head>
<meta charset="utf-8">
<title>nuvae – Alpine Edelweiss Wrap label</title>
<link rel="stylesheet" href="https://fonts.googleapis.com/css2?family=Quicksand:wght@300&family=Barlow+Semi+Condensed:wght@400&family=Montserrat:wght@400&display=swap">
<style>
  :root {
    --backdrop: #e4e6ea;
    --label-black: #2c2c2d;
    --label-ink: #f2f2f2;
    --label-ink-soft: #d6d6d6;
    --art-tone: #3a3a3c;
    --cap-gold: #d9cf9f;
    --cap-gold-edge: #b8ab72;
  }
  * { box-sizing: border-box; margin: 0; padding: 0; }
  html, body {
    width: 1200px; height: 810px; overflow: hidden;
    background: var(--backdrop);
  }
  .canvas {
    position: relative; width: 1200px; height: 810px;
  }
  .front-label {
    position: absolute; left: 300px; top: 100px;
    width: 370px; height: 610px;
    background: var(--label-black);
    color: var(--label-ink);
    display: flex; flex-direction: column; align-items: center;
    text-align: center;
  }
  .brand-name {
    margin-top: 48px;
    font-family: "Quicksand", sans-serif;
    font-weight: 300;
    font-size: 110px;
    line-height: 1;
    letter-spacing: 1px;
  }
  .product-name {
    margin-top: 16px;
    font-family: "Barlow Semi Condensed", sans-serif;
    font-size: 33px;
    line-height: 1;
  }
  .product-tagline {
    margin-top: 4px;
    font-family: "Montserrat", sans-serif;
    font-size: 11px;
    color: var(--label-ink-soft);
  }
  .fruit-art {
    margin-top: 26px;
    width: 190px; height: 200px;
    background: radial-gradient(circle at 50% 65%, #4a4a4c 0%, var(--art-tone) 70%);
    border-radius: 6px;
  }
  .scent-name {
    margin-top: 16px;
    font-family: "Barlow Semi Condensed", sans-serif;
    font-size: 34px;
    line-height: 1;
  }
  .ingredients {
    margin-top: 18px;
    width: 310px;
    font-family: "Montserrat", sans-serif;
    font-size: 11px;
    line-height: 1.4;
    color: var(--label-ink-soft);
  }
  .cap-label {
    position: absolute; left: 745px; top: 250px;
    width: 320px; height: 320px;
  }
</style>
</head>
<body>
<main class="canvas">
  <section class="front-label">
    <h1 class="brand-name">nuvae</h1>
    <h2 class="product-name">Alpine Edelweiss Wrap</h2>
    <p class="product-tagline">No-Needle Contour Treatment</p>
    <div class="fruit-art" role="img" aria-label="Line drawing of a pair of cherries on a stem with a leaf"></div>
    <p class="scent-name">Cherry blossom</p>
    <p class="ingredients">Ingredients that have scientific proof of anti aging: Cherry blossom extact, collegen, hyaluronic acid, coconut oil.</p>
  </section>

  <svg class="cap-label" viewBox="0 0 320 320" aria-label="Round lid sticker">
    <circle cx="160" cy="160" r="156" fill="var(--cap-gold)" stroke="var(--cap-gold-edge)" stroke-width="2"/>
    <circle cx="160" cy="160" r="144" fill="var(--label-black)"/>
    <rect x="80" y="70" width="160" height="180" rx="6" fill="var(--art-tone)" role="img" aria-label="Line drawing of a pair of cherries on a stem with a leaf"/>
  </svg>
</main>
</body>
</html>
```